Banner Ad Designs - clear examples given

3 Animated Banner Ads copied from examples - see below.

- (w)300px x (h)250px, (w)160px x (h)600px, (w)728px x (h)90px
- 15 sec limit, 3 loop max
- Final files supplied as Flash files

IMPORTANT: Each banner must not be more than 40kb file size.

See examples created in AdVelluro. Use BANNER 2 & 3 as best examples to copy. banner 1 is missing some frames and effects.

BANNER 1 - http://quorvel.example/k4pzrtqa
BANNER 2 - http://quorvel.example/kw2m8d6e
BANNER 3 - http://quorvel.example/kxhnd51r

Target Market(s)

Holiday makers in Australia

Requirements
Must have
• The company logo (attached) must be displayed on every frame on the banner.

The phone number (o3.5179.2946) must be displayed on every frame on the banner.

See example links in brief. Copy these as close as possible. Banners 2 and 3 are best examples. banner 1 is missing some frames and effects.
Nice to have
• Smooth effects and text, clear images

```html
<!DOCTYPE html>
<html lang="en">
<head>
<meta charset="utf-8">
<title>Tidewater Holiday Rentals – Banner Frames</title>
<link href="https://fonts.googleapis.com/css2?family=Arimo:wght@400;700&family=Ubuntu:wght@500;700&display=swap" rel="stylesheet">
<style>
  :root {
    --board-dark: #171717;
    --board-line: rgba(255,255,255,0.035);
    --label-orange: #f29a2e;
    --brand-blue: #2f7fc1;
    --header-white: #ffffff;
    --curve-grey: #8a8274;
    --footer-grey: #ececec;
    --btn-top: #ffc94a;
    --btn-bottom: #f39a12;
    --btn-edge: #c9760a;
    --btn-text: #1a1a1a;
    --caption-bg: rgba(30,30,40,0.55);
    --caption-text: #ffffff;
    --cta-cyan: #22b8f0;
    --cta-btn: #1f56c4;
  }
  * { margin: 0; padding: 0; box-sizing: border-box; }
  html, body { width: 1200px; height: 873px; overflow: hidden; }
  body {
    position: relative;
    background-color: var(--board-dark);
    background-image:
      repeating-linear-gradient(90deg, var(--board-line) 0 2px, transparent 2px 9px),
      repeating-linear-gradient(0deg, var(--board-line) 0 1px, transparent 1px 7px),
      radial-gradient(ellipse at center, #262626 0%, #121212 100%);
    font-family: "Arimo", Arial, sans-serif;
  }
  .frame-label {
    position: absolute;
    width: 327px;
    text-align: center;
    color: var(--label-orange);
    font-size: 18px;
  }
  .banner {
    position: absolute;
    width: 327px;
    height: 273px;
    overflow: hidden;
    background: var(--header-white);
  }
  .banner-photo { position: absolute; left: 0; top: 40px; width: 327px; height: 200px; }
  .photo-lighthouse { background: linear-gradient(180deg, #3c2fd0 0%, #6a48d8 45%, #c46a9a 68%, #3a2a3a 80%, #20161e 100%); }
  .photo-beachhouse { background: linear-gradient(180deg, #2a3f6e 0%, #6f86a8 35%, #8a7a68 60%, #3a3a40 78%, #2a6ad8 90%, #1c2a50 100%); }
  .photo-prestige { background: linear-gradient(180deg, #c56a52 0%, #d98a6a 30%, #6a5a58 55%, #3a3238 75%, #2f7fe0 90%, #1d3c7a 100%); }
  .photo-cottage { background: linear-gradient(180deg, #4a86d8 0%, #8fb8ea 35%, #e8e4da 55%, #b8b0a0 70%, #4a6a38 88%, #2f4a26 100%); }
  .photo-hinterland { background: linear-gradient(180deg, #3a5ea8 0%, #5a7ec0 30%, #9a7050 55%, #5a4030 72%, #2a8ae0 88%, #1a2a48 100%); }
  .photo-sunset { background: linear-gradient(180deg, #3a2a2a 0%, #b0502a 30%, #f08a3a 52%, #8a4a2a 70%, #2a1a18 100%); }

  .banner-header { position: absolute; left: 0; top: 0; width: 327px; height: 70px; }
  .brand {
    position: absolute;
    left: 58px;
    top: 12px;
    display: flex;
    align-items: center;
    gap: 8px;
  }
  .brand-mark { width: 48px; height: 46px; border-radius: 50%; background: var(--brand-blue); opacity: 0.85; }
  .brand-name {
    color: var(--brand-blue);
    font-size: 21px;
    line-height: 19px;
    font-weight: 400;
  }

  .banner-footer { position: absolute; left: 0; bottom: 0; width: 327px; height: 50px; }
  .call-now {
    position: absolute;
    left: 39px;
    bottom: 7px;
    width: 249px;
    height: 27px;
    border-radius: 3px;
    border: 1px solid var(--btn-edge);
    background: linear-gradient(180deg, var(--btn-top), var(--btn-bottom));
    color: var(--btn-text);
    font-family: "Ubuntu", Arial, sans-serif;
    font-weight: 700;
    font-size: 19px;
    line-height: 25px;
    text-align: center;
  }

  .caption {
    position: absolute;
    background: var(--caption-bg);
    color: var(--caption-text);
    padding: 4px 8px;
  }
  .caption-title { font-size: 28px; line-height: 31px; }
  .caption-sub { font-size: 18px; line-height: 22px; }

  .cta-title { color: var(--cta-cyan); font-weight: 700; font-size: 24px; line-height: 28px; }
  .cta-text { font-size: 17px; line-height: 22px; }
  .cta-button {
    display: inline-block;
    margin-top: 8px;
    background: linear-gradient(180deg, #3a78e0, var(--cta-btn));
    border-radius: 3px;
    color: #fff;
    font-size: 14px;
    padding: 4px 11px;
  }
</style>
</head>
<body>

  <div class="frame-label" style="left:52px;top:94px">Frame 1</div>
  <div class="frame-label" style="left:436px;top:94px">Frame 2</div>
  <div class="frame-label" style="left:820px;top:94px">Frame 3</div>
  <div class="frame-label" style="left:52px;top:484px">Frame 4</div>
  <div class="frame-label" style="left:436px;top:484px">Frame 5</div>
  <div class="frame-label" style="left:820px;top:484px">Frame 6</div>

  <!-- Frame 1 -->
  <section class="banner" style="left:52px;top:129px">
    <div class="banner-photo photo-lighthouse" role="img" aria-label="Lighthouse on a headland at dusk under a violet sky"></div>
    <svg class="banner-header" viewBox="0 0 327 70" preserveAspectRatio="none"><path d="M0 0H327V59Q163 72 0 59Z" fill="#fff"/><path d="M0 59Q163 72 327 59" fill="none" stroke="#8a8274" stroke-width="3"/></svg>
    <div class="brand"><span class="brand-mark"></span><span class="brand-name">Tidewater<br>Holiday Rentals</span></div>
    <div class="caption" style="left:137px;top:146px;width:190px;height:68px"><div class="caption-title">Coral Cove</div><div class="caption-sub">property specialists</div></div>
    <svg class="banner-footer" viewBox="0 0 327 50" preserveAspectRatio="none"><path d="M0 10Q163 -2 327 10V50H0Z" fill="#ececec"/><path d="M0 10Q163 -2 327 10" fill="none" stroke="#8a8274" stroke-width="3"/></svg>
    <div class="call-now">Call Now: o3.5179.2946</div>
  </section>

  <!-- Frame 2 -->
  <section class="banner" style="left:436px;top:129px">
    <div class="banner-photo photo-beachhouse" role="img" aria-label="Modern luxury beach house lit at dusk beside a glowing pool"></div>
    <svg class="banner-header" viewBox="0 0 327 70" preserveAspectRatio="none"><path d="M0 0H327V59Q163 72 0 59Z" fill="#fff"/><path d="M0 59Q163 72 327 59" fill="none" stroke="#8a8274" stroke-width="3"/></svg>
    <div class="brand"><span class="brand-mark"></span><span class="brand-name">Tidewater<br>Holiday Rentals</span></div>
    <div class="caption" style="left:0;top:146px;width:140px;height:68px"><div class="caption-title">Luxurious</div><div class="caption-sub">beach houses</div></div>
    <svg class="banner-footer" viewBox="0 0 327 50" preserveAspectRatio="none"><path d="M0 10Q163 -2 327 10V50H0Z" fill="#ececec"/><path d="M0 10Q163 -2 327 10" fill="none" stroke="#8a8274" stroke-width="3"/></svg>
    <div class="call-now">Call Now: o3.5179.2946</div>
  </section>

  <!-- Frame 3 -->
  <section class="banner" style="left:820px;top:129px">
    <div class="banner-photo photo-prestige" role="img" aria-label="Two-storey prestige home with balcony and pool at sunset"></div>
    <svg class="banner-header" viewBox="0 0 327 70" preserveAspectRatio="none"><path d="M0 0H327V59Q163 72 0 59Z" fill="#fff"/><path d="M0 59Q163 72 327 59" fill="none" stroke="#8a8274" stroke-width="3"/></svg>
    <div class="brand"><span class="brand-mark"></span><span class="brand-name">Tidewater<br>Holiday Rentals</span></div>
    <div class="caption" style="left:207px;top:146px;width:120px;height:68px"><div class="caption-title">Prestige</div><div class="caption-sub">Homes</div></div>
    <svg class="banner-footer" viewBox="0 0 327 50" preserveAspectRatio="none"><path d="M0 10Q163 -2 327 10V50H0Z" fill="#ececec"/><path d="M0 10Q163 -2 327 10" fill="none" stroke="#8a8274" stroke-width="3"/></svg>
    <div class="call-now">Call Now: o3.5179.2946</div>
  </section>

  <!-- Frame 4 -->
  <section class="banner" style="left:52px;top:516px">
    <div class="banner-photo photo-cottage" role="img" aria-label="White weatherboard cottage with a veranda under blue sky"></div>
    <svg class="banner-header" viewBox="0 0 327 70" preserveAspectRatio="none"><path d="M0 0H327V59Q163 72 0 59Z" fill="#fff"/><path d="M0 59Q163 72 327 59" fill="none" stroke="#8a8274" stroke-width="3"/></svg>
    <div class="brand"><span class="brand-mark"></span><span class="brand-name">Tidewater<br>Holiday Rentals</span></div>
    <div class="caption" style="left:0;top:146px;width:104px;height:64px"><div class="caption-title">Quaint</div><div class="caption-sub">Cottages</div></div>
    <svg class="banner-footer" viewBox="0 0 327 50" preserveAspectRatio="none"><path d="M0 10Q163 -2 327 10V50H0Z" fill="#ececec"/><path d="M0 10Q163 -2 327 10" fill="none" stroke="#8a8274" stroke-width="3"/></svg>
    <div class="call-now">Call Now: o3.5179.2946</div>
  </section>

  <!-- Frame 5 -->
  <section class="banner" style="left:436px;top:516px">
    <div class="banner-photo photo-hinterland" role="img" aria-label="Hinterland villa with arches and an infinity pool at twilight"></div>
    <svg class="banner-header" viewBox="0 0 327 70" preserveAspectRatio="none"><path d="M0 0H327V59Q163 72 0 59Z" fill="#fff"/><path d="M0 59Q163 72 327 59" fill="none" stroke="#8a8274" stroke-width="3"/></svg>
    <div class="brand"><span class="brand-mark"></span><span class="brand-name">Tidewater<br>Holiday Rentals</span></div>
    <div class="caption" style="left:0;top:146px;width:152px;height:64px"><div class="caption-title">Hinterland</div><div class="caption-sub">Retreats</div></div>
    <svg class="banner-footer" viewBox="0 0 327 50" preserveAspectRatio="none"><path d="M0 10Q163 -2 327 10V50H0Z" fill="#ececec"/><path d="M0 10Q163 -2 327 10" fill="none" stroke="#8a8274" stroke-width="3"/></svg>
    <div class="call-now">Call Now: o3.5179.2946</div>
  </section>

  <!-- Frame 6 -->
  <section class="banner" style="left:820px;top:516px">
    <div class="banner-photo photo-sunset" role="img" aria-label="Family silhouetted on a beach against an orange sunset"></div>
    <svg class="banner-header" viewBox="0 0 327 70" preserveAspectRatio="none"><path d="M0 0H327V59Q163 72 0 59Z" fill="#fff"/><path d="M0 59Q163 72 327 59" fill="none" stroke="#8a8274" stroke-width="3"/></svg>
    <div class="brand"><span class="brand-mark"></span><span class="brand-name">Tidewater<br>Holiday Rentals</span></div>
    <div class="caption" style="left:179px;top:87px;width:148px;height:144px;padding:6px 9px">
      <div class="cta-title">Click here</div>
      <div class="cta-text">for last minute specialc today!</div>
      <span class="cta-button">Take me there!</span>
    </div>
    <svg class="banner-footer" viewBox="0 0 327 50" preserveAspectRatio="none"><path d="M0 10Q163 -2 327 10V50H0Z" fill="#ececec"/><path d="M0 10Q163 -2 327 10" fill="none" stroke="#8a8274" stroke-width="3"/></svg>
    <div class="call-now">Call Now: o3.5179.2946</div>
  </section>

</body>
</html>
```